Disability Service Provider Expo Banner that will stand out amongst the competition

We would like to have a two banners designed to be able to display at expos that outline the services that we provide as a company. We are a disability service provider who aims to provider services to increase the independence of those living with a disability. We would like the banners to follow consistent themes/designs from other marketing material that we have (see brief for designs). One of the banners will be for the allied health services we provide (exercise physiology and occupational therapy) and the other banner will be promoting the our support worker, programs, and short-term accommodation. Our main colour schemes for therapy are black, yellow, and white. For our other services we utilise yellow, blue, and magenta as part of our colour pallet. Please utilise the information from the flyers, colours, and logos all located in the design brief. The style of banner can be seen in the images upload in the brief.

Target Market(s)

Parents and carers of those who livce with a disability, and seeking their business over our competitors

Industry/Entity Type

Disability Service and Health Provider

Colors

Designer to choose colors to be used in the design.

Requirements
Must have
• Eye catching, limited text
Nice to have
• Split services across a few banners
Should not have
• Lots of words

```html
<!DOCTYPE html>
<html lang="en">
<head>
<meta charset="utf-8">
<title>Brightvale Expo Banners</title>
<link rel="stylesheet" href="https://fonts.googleapis.com/css2?family=Montserrat:ital,wght@0,400;0,500;0,700;0,800;1,500&family=Gochi+Hand&family=Short+Stack&display=swap">
<style>
  :root{
    --stage:#9d9d9d;
    --ink:#111111;
    --paper:#ffffff;
    --sun:#f5d81c;
    --magenta:#e8135f;
    --sky:#4aa8e0;
    --pill:#4a8fd4;
    --photo-gym:#7f93b0;
    --photo-warm:#b49a86;
    --photo-park:#8a9170;
    --photo-room:#c9c4c8;
  }
  *{box-sizing:border-box;margin:0;padding:0}
  html,body{width:1200px;height:1117px;overflow:hidden;background:var(--stage)}
  .canvas{position:relative;width:1200px;height:1117px}
  .banner{position:absolute;top:140px;width:360px;height:834px;overflow:hidden;background:var(--paper)}
  .banner--therapy{left:195px}
  .banner--support{left:635px}
  .abs{position:absolute}
  .brand-dot{position:absolute;left:50%;width:40px;height:40px;margin-left:-20px;border-radius:50%;background:var(--sun)}
  .brand-name{position:absolute;left:0;width:100%;text-align:center;font:800 48px/1 "Montserrat",sans-serif;letter-spacing:-1px}
  .taglines{position:absolute;left:0;width:100%;display:flex;justify-content:center;align-items:center;gap:14px;font:400 12px/1 "Gochi Hand",cursive;text-transform:uppercase;color:var(--ink)}
  .taglines i{width:12px;height:12px;border-radius:50%;background:var(--sun);display:block}
  .photo{position:absolute}
  /* therapy banner */
  .therapy-header{top:0;left:0}
  .therapy-heading{top:212px;left:0;width:100%;text-align:center;font:800 20px/1 "Montserrat",sans-serif;color:var(--ink)}
  .therapy-heading .boxed{display:inline-block;margin-top:4px;padding:4px 8px;background:var(--ink);color:var(--paper)}
  .therapy-heading .boxed em{font-style:normal;color:var(--sun)}
  .therapy-intro{top:283px;left:40px;width:280px;text-align:center;font:italic 500 11.5px/1.2 "Montserrat",sans-serif;color:var(--ink)}
  .therapy-lower{top:540px;left:0;width:360px;height:230px;background:var(--ink)}
  .photo--framed{border:3px solid var(--sun);border-radius:10px}
  .therapy-body{top:640px;left:28px;width:304px;text-align:center;font:500 10.3px/1.22 "Montserrat",sans-serif;color:var(--paper)}
  .therapy-url{top:780px;left:0;width:100%;text-align:center;font:700 16px/1 "Montserrat",sans-serif;color:var(--ink)}
  /* support banner */
  .circle{position:absolute;border-radius:50%}
  .support-band{top:200px;left:0;width:360px;height:80px;background:var(--magenta);clip-path:polygon(3% 8%,60% 0,100% 6%,100% 92%,55% 100%,0 96%,2% 50%)}
  .support-band-text{top:214px;left:0;width:360px;text-align:center;font:400 19px/1.1 "Gochi Hand",cursive;color:var(--paper);text-transform:uppercase}
  .support-intro{top:288px;left:30px;width:300px;text-align:center;font:400 11.5px/1.2 "Short Stack",cursive;color:var(--ink)}
  .photo--rounded{border-radius:14px}
  .support-body{top:643px;left:28px;width:304px;text-align:center;font:400 10.2px/1.22 "Montserrat",sans-serif;color:var(--ink)}
  .support-url{top:773px;left:28px;width:270px;height:30px;border-radius:15px;background:var(--pill);color:var(--paper);font:700 15px/30px "Montserrat",sans-serif;padding-left:16px}
</style>
</head>
<body>
<main class="canvas">

  <section class="banner banner--therapy" aria-label="Allied health banner">
    <svg class="abs therapy-header" width="360" height="200" viewBox="0 0 360 200" aria-hidden="true">
      <path d="M0 0H360V128C300 160 240 168 170 162C100 156 50 162 0 188Z" fill="var(--ink)"/>
      <path d="M0 188C50 162 100 156 170 162C240 168 300 160 360 128V136C300 170 240 176 170 170C100 164 50 170 0 196Z" fill="var(--sun)"/>
    </svg>
    <div class="brand-dot" style="top:38px"></div>
    <div class="brand-name" style="top:92px;color:var(--paper)">BRIGHTVALE</div>

    <div class="taglines" style="top:200px"><span>More independance</span><i></i><span>More choice</span><i></i><span>More fun</span></div>

    <h2 class="abs therapy-heading">EXERCISE PHYSIOLOGY &amp;<br><span class="boxed">OCCUPATIONAL <em>THERAPY</em></span></h2>
    <p class="abs therapy-intro">Improve your health, quality of life, and independence with the help of our Exercise Physiologist!</p>

    <div class="photo" style="top:330px;left:0;width:360px;height:215px;background:linear-gradient(135deg,#dfe6ee,var(--photo-gym) 55%,#2a3550)" role="img" aria-label="Photo: exercise physiologist guiding a client through a floor exercise in a gym"></div>
    <div class="abs therapy-lower"></div>
    <div class="photo photo--framed" style="top:522px;left:20px;width:155px;height:102px;background:linear-gradient(135deg,#d6d6d6,#6a6e78)" role="img" aria-label="Photo: trainer assisting a wheelchair user with a resistance cable"></div>
    <div class="photo photo--framed" style="top:524px;left:181px;width:161px;height:102px;background:linear-gradient(135deg,var(--photo-park),#d07aa8)" role="img" aria-label="Photo: two women stretching outdoors by a lake"></div>

    <p class="abs therapy-body">At Brightvale, we believe that every person should have the opportunity to live an active, happy, and full life. For some, this can be limited by their physical or mental health and be tough to overcome on their own. With the help of our exercise physiologists, we can assist you to achieve your health and well-being and independence goals.</p>

    <svg class="abs" style="top:740px;left:0" width="360" height="94" viewBox="0 0 360 94" aria-hidden="true">
      <rect width="360" height="94" fill="var(--paper)"/>
      <path d="M0 0H360V30C300 14 240 10 170 14C100 18 50 16 0 4Z" fill="var(--ink)"/>
      <path d="M200 14C260 12 310 20 360 44V52C310 30 260 20 200 18Z" fill="var(--sun)"/>
    </svg>
    <div class="abs therapy-url">www.brightvale.com.au</div>
  </section>

  <section class="banner banner--support" aria-label="Support services banner">
    <div class="circle" style="top:-20px;left:-10px;width:110px;height:110px;background:var(--sky)"></div>
    <div class="circle" style="top:48px;left:-18px;width:68px;height:68px;background:var(--magenta)"></div>
    <div class="circle" style="top:-26px;left:264px;width:78px;height:78px;background:var(--sun)"></div>

    <div class="brand-dot" style="top:40px"></div>
    <div class="brand-name" style="top:100px;color:var(--ink)">BRIGHTVALE</div>

    <div class="taglines" style="top:172px"><span>More independance</span><i></i><span>More choice</span><i></i><span>More fun</span></div>

    <div class="abs support-band"></div>
    <h2 class="abs support-band-text">Our support worker, programs,<br>and short-term accommodation.</h2>
    <p class="abs support-intro">Supporting you to develop independence. Helping you to engage in community, social &amp; recreactional activities.</p>

    <div class="photo" style="top:340px;left:0;width:246px;height:138px;border-radius:0 14px 14px 0;background:linear-gradient(135deg,var(--photo-park),#3c4350)" role="img" aria-label="Photo: three friends in wheelchairs together in a park"></div>
    <div class="photo" style="top:340px;left:254px;width:106px;height:136px;border-radius:14px 0 0 14px;background:linear-gradient(135deg,var(--photo-room),var(--photo-warm))" role="img" aria-label="Photo: two women sharing cupcakes and laughing"></div>
    <div class="photo photo--rounded" style="top:485px;left:18px;width:113px;height:138px;background:linear-gradient(135deg,#6b4a3a,#d8b79c)" role="img" aria-label="Photo: two young women smiling together"></div>
    <div class="photo photo--rounded" style="top:483px;left:138px;width:204px;height:130px;background:linear-gradient(135deg,var(--photo-room),#8899aa)" role="img" aria-label="Photo: support worker and young woman building with colourful blocks"></div>

    <p class="abs support-body">We have a team who is experienced, passionate, dedicated &amp; FUN! We enjoy finding ways to provide social, recreational &amp; community participation opportunities for young people with mild to moderate disabilities &amp; mental health conditions. Our unique, real-life experiences are specifically tailored for this age group &amp; promote capacity building in a fun, safe, supportive, &amp; age-appropriate setting. We find that this approach strengthens social connection, confidence &amp; inclusion.</p>

    <div class="circle" style="top:738px;left:282px;width:90px;height:90px;background:var(--magenta)"></div>
    <div class="abs support-url">www.brightvale.com.au</div>
    <div class="circle" style="top:772px;left:256px;width:56px;height:56px;background:var(--sun)"></div>
  </section>

</main>
</body>
</html>
```